High end business card design for custom homebuilding company

Looking for a high end business card design that is unique and elegant. Can use embossing, foil printing, laser die cutting, or any high end printing technique or high end paper. Will upload current design so you can see the logo and what we are using currently, but we want something more unique and elegant. I included our logo to help with design.

Target Market(s)

High end custom home buyers of $1.5 million plus homes. Also real estate developers of high end communities.

Industry/Entity Type

Business

Contact Information for Business Card

Double sided. We want something very elegant and expensive looking. We are looking to incorporate a combination of perhaps linen paper or a high end paper, with foil stamping or embossing/debossing to make the card look unique, but still elegant. We tend to use blacks and golds, but are open to any ideas. Looking for creative and unique design.

Colors

Designer to choose colors to be used in the design.

Requirements
Must have
• High end, elegant look. Can use foil, embossing, or high end papers like linen. We want to make the card unique and interesting, but elegant and expensive looking.
Nice to have
• I am including just some cards I saw that looked interesting for one reason or another. I like a clean elegant design and like both the clean white style, and the blacks. So not sure if we want a black design or white. Would like to see both.

```html
<!DOCTYPE html>
<html lang="en">
<head>
<meta charset="utf-8">
<title>Brightmoor Custom Homes – Business Card</title>
<link href="https://fonts.googleapis.com/css2?family=Source+Sans+3:wght@400;600&display=swap" rel="stylesheet">
<style>
  :root {
    --backdrop: #000000;
    --card: #323336;
    --card-edge: #2c2d30;
    --gold: #c9b23c;
    --accent: #e3df4c;
    --ink: #f2f2f2;
    --rule: #4a4b4f;
  }
  * { margin: 0; padding: 0; box-sizing: border-box; }
  html, body {
    width: 1200px; height: 900px; overflow: hidden;
    background: var(--backdrop);
    font-family: "Source Sans 3", "Helvetica Neue", Arial, sans-serif;
    color: var(--ink);
  }
  .stage { position: relative; width: 1200px; height: 900px; }
  .card {
    position: absolute; top: 271px;
    width: 457px; height: 281px;
    border-radius: 14px;
    overflow: hidden;
    background: radial-gradient(ellipse at 50% 40%, #37383b 0%, var(--card) 55%, var(--card-edge) 100%);
  }
  .card--front { left: 137px; }
  .card--back { left: 626px; }

  .brand-dot { width: 14px; height: 14px; border-radius: 50%; background: var(--gold); flex: none; }
  .brand-name {
    font-weight: 600; color: var(--gold);
    text-transform: uppercase; white-space: nowrap;
  }

  .brand-mark {
    position: absolute; left: 28px; top: 127px; width: 180px;
    display: flex; align-items: center; justify-content: center; gap: 9px;
  }
  .brand-mark .brand-name { font-size: 18px; letter-spacing: 1.5px; }
  .brand-mark .brand-dot { width: 12px; height: 12px; }

  .divider {
    position: absolute; left: 221px; top: 91px; width: 1px; height: 180px;
    background: linear-gradient(to bottom, transparent, var(--rule) 20%, var(--rule) 80%, transparent);
  }
  .contact { position: absolute; left: 252px; top: 49px; }
  .contact__name { font-weight: 600; font-size: 12.5px; color: var(--accent); letter-spacing: .3px; }
  .contact__role { font-size: 9px; margin-top: 3px; letter-spacing: .3px; }
  .contact__list { list-style: none; margin-top: 10px; }
  .contact__list li {
    display: flex; align-items: center; height: 17px; font-size: 12.5px;
  }
  .contact__list li.address { align-items: flex-start; height: auto; margin-top: 15px; line-height: 17px; }
  .icon { width: 8px; height: 8px; margin: 0 11px 0 3px; fill: var(--accent); flex: none; }
  .address .icon { margin-top: 5px; }

  .wordmark {
    position: absolute; left: 0; right: 0; top: 127px;
    display: flex; align-items: center; justify-content: center; gap: 12px;
  }
  .wordmark .brand-name { font-size: 22px; letter-spacing: 2px; }
  .wordmark .brand-dot { width: 16px; height: 16px; }
</style>
</head>
<body>
<main class="stage">
  <section class="card card--front">
    <div class="brand-mark">
      <span class="brand-dot"></span>
      <span class="brand-name">Brightmoor</span>
    </div>
    <div class="divider"></div>
    <div class="contact">
      <p class="contact__name">LORUM SMITH</p>
      <p class="contact__role">MANAGING DIRECTOR</p>
      <ul class="contact__list">
        <li><svg class="icon" viewBox="0 0 10 10"><path d="M2 0l2 2.5-1.2 1.2c.6 1.4 1.7 2.5 3.1 3.1L7.1 5.6 10 7.5 8.6 10C4 9.6.4 6 0 1.4z"/></svg>444 555 6688</li>
        <li><svg class="icon" viewBox="0 0 10 10"><path d="M2.5 0h5v10h-5zM3.5 1v7h3V1z"/></svg>888 444 0000</li>
        <li><svg class="icon" viewBox="0 0 10 10"><path d="M0 2h10v6H0zM1 3v.4l4 2.4 4-2.4V3z"/></svg>info@webname.com</li>
        <li><svg class="icon" viewBox="0 0 10 10"><circle cx="5" cy="5" r="5"/></svg>www.webaddress.com</li>
        <li class="address"><svg class="icon" viewBox="0 0 10 10"><path d="M5 0a3.6 3.6 0 0 1 3.6 3.6C8.6 6.2 5 10 5 10S1.4 6.2 1.4 3.6A3.6 3.6 0 0 1 5 0zm0 2.2a1.4 1.4 0 1 0 0 2.8 1.4 1.4 0 0 0 0-2.8z"/></svg><span>421, Address line here,<br>Dummy Code, 45452<br>Country Name</span></li>
      </ul>
    </div>
  </section>

  <section class="card card--back">
    <div class="wordmark">
      <span class="brand-dot"></span>
      <span class="brand-name">Brightmoor Custom Homes</span>
    </div>
  </section>
</main>
</body>
</html>
```